Business Card Design Project

I need a business card design for an Organic drive thru coffee kiosk. We will serve organic coffee, teas & smoothies and will serve healthy breakfast food/snacks for people on the go.
I want the card to have 2-3 colors max (earthy colors like browns, greens and so on).
I have attached the logo I want used and would love to play off the theme of "balance."
Include:
Fair-Leaf Coffee
address: 3170 Morrow Ct. Raleigh, NC 27493
phone: 919-371-4402
website: www.fair-leaf.com (website is not up yet but still include it on card)
email: Joanne@fair-leaf.com
I want one of the following sayings somewhere on the card (the front or back is fine):
"Eat & Drink Fair, on the run!"
"Break the fast with Fair-Leaf"
Maybe on the back list what we offer:
-Organic coffee, espresso & tea
-Quorblend smoothies & protein shakes
-Zippy Press (100% fresh local fruit and veggies)
-Healthy Bites
Target Market(s)
College age to 55
Industry/Entity Type
Business
Look and feel
Each slider illustrates characteristics of the customer's brand and the style your logo design should communicate.

```html
<!DOCTYPE html>
<html lang="en">
<head>
<meta charset="utf-8">
<title>Fair-Leaf Business Card</title>
<link rel="stylesheet" href="https://fonts.googleapis.com/css2?family=Questrial&display=swap">
<style>
  :root {
    --backdrop: #56656a;
    --espresso: #2e2416;
    --sun: #f0d000;
    --label: #f2c200;
    --bean: #5b2a1e;
    --ink: #3a2418;
    --paper: #ffffff;
    --mist: #ece4e4;
    --rule: #c9c0b8;
  }
  html, body {
    margin: 0;
    width: 1200px;
    height: 900px;
    overflow: hidden;
    background: var(--backdrop);
    font-family: "Questrial", "Century Gothic", sans-serif;
  }
  .card {
    position: absolute;
    top: 282px;
    width: 505px;
    height: 305px;
    box-shadow: 0 6px 14px rgba(0,0,0,0.35);
  }
  .card-front { left: 80px; background: var(--espresso); }
  .card-back { left: 625px; background: var(--paper); }

  .mark-dot { position: absolute; border-radius: 50%; }
  .brand { position: absolute; margin: 0; font-weight: 400; white-space: nowrap; }

  .card-front .mark-dot { left: 226px; top: 66px; width: 46px; height: 46px; background: var(--sun); }
  .card-front .brand {
    left: 0; right: 0; top: 118px; text-align: center;
    font-size: 46px; color: var(--sun); letter-spacing: 1px;
  }
  .sayings {
    position: absolute; left: 0; right: 0; top: 237px; margin: 0;
    text-align: center; font-size: 13.5px; color: var(--sun); white-space: nowrap;
  }
  .sayings span + span { margin-left: 8px; }

  .card-back .mark-dot { left: 98px; top: 60px; width: 36px; height: 36px; background: var(--bean); }
  .card-back .brand {
    left: 55px; top: 100px; font-size: 34px; color: var(--bean);
  }
  .accent-circle {
    position: absolute; left: 333px; top: 52px; width: 128px; height: 128px;
    border-radius: 50%; background: var(--mist);
  }
  .contact {
    position: absolute; right: 47px; top: 194px; text-align: right; color: var(--ink);
    white-space: nowrap;
  }
  .person { margin: 0 8px 8px 0; font-size: 14.5px; }
  .contact-line { margin: 0 0 6px; font-size: 12.8px; }
  .contact-line b { font-weight: 400; color: var(--label); margin-right: 4px; }
  .sep { display: inline-block; width: 1px; height: 13px; background: var(--rule); margin: 0 6px -2px; }
</style>
</head>
<body>
  <section class="card card-front">
    <span class="mark-dot"></span>
    <h1 class="brand">Fair-Leaf</h1>
    <p class="sayings"><span>"Eat &amp; Drink Fair, on the run!"</span><span>"Break the fast with Fair-Leaf"</span></p>
  </section>

  <section class="card card-back">
    <span class="mark-dot"></span>
    <h2 class="brand">Fair-Leaf</h2>
    <span class="accent-circle"></span>
    <div class="contact">
      <p class="person">Joanne</p>
      <p class="contact-line"><b>A.</b>3170 Morrow Ct. Raleigh, NC 27493<span class="sep"></span><b>P.</b>919-371-4402</p>
      <p class="contact-line"><b>W.</b>www.fair-leaf.com<span class="sep"></span><b>E.</b>Joanne@fair-leaf.com</p>
    </div>
  </section>
</body>
</html>
```